Labels for Bees Wax Candles & Honey Jars

We need labels for jars of natural honey. Most of our jars are square and the labels about 2" by 2".

Also we make bees wax candles of various sizes. We wish to wrap th enables around the circular candles which are between 2" and 3" in diameter... thus another have inch per label so they can be attached adhesively. The candles also vary in height... therefor th enables need to be 1.5", 2" and 3" in height.

We ar elooking for a very artistic and simple label that may include vibrant colors.
The name of our company must be displayed.. Candles by Morton and for the Honey.... Morton's All Natural Honey

The labels will be used for both Honey Jars as well as Bees Wax candles. There will be various sizes but that is something that can be adjusted after the initial design is approved. The Honey Jars should read "Natural Honey by Morton" and the Candle labels should read "Natural Bees Wax Candles by Morton" I am interested in simple, colorful, legible, and arty labels that pertain to bees and the natural environment. Hope this helps. We may also use a similar design on our web page. The size of the label on the honey will be 2" by 2" and the candles will vary.

Target Market(s)

Individual that purchase natural and organic products.

Requirements
Must have
• Labels should be very creative but legible and the emphasis on the candles should be all natural bees wax and the emphasis on the honey should be all natural honey. We are talking about the same design but different sizes and names.
Nice to have
• brillant colors and artistic

```html
<!DOCTYPE html>
<html lang="en">
<head>
<meta charset="utf-8">
<title>Natural Honey by Morton – Jar Label</title>
<link rel="stylesheet" href="https://fonts.googleapis.com/css2?family=Cinzel:wght@400&family=Federo&display=swap">
<style>
  :root {
    --page: #ffffff;
    --ink: #1b1712;
    --rust: #a8422a;
    --pink: #f3a2d4;
    --cream: #ece6da;
    --peach: #f2c9a0;
    --amber: #f0a03a;
    --deep-amber: #e58a17;
    --comb-light: #f3a640;
    --comb-dark: #e27f0c;
    --gold-light: #f4dc8a;
    --gold: #c99a2e;
    --gold-dark: #7e5a12;
    --bar-dark: #4a4234;
    --bar-light: #a59a78;
    --bar-text: #f4f0e4;
    --hex: rgba(255, 240, 220, 0.32);
  }
  * { box-sizing: border-box; margin: 0; padding: 0; }
  html, body { width: 1200px; height: 1177px; overflow: hidden; background: var(--page); }

  .label {
    position: absolute;
    left: 91px; top: 72px;
    width: 1005px; height: 1010px;
    overflow: hidden;
  }

  .foil-top {
    position: absolute; left: 0; top: 0; width: 100%; height: 37px;
    background: linear-gradient(100deg, var(--gold-dark), var(--gold-light) 25%, var(--gold) 50%, var(--gold-light) 75%, var(--gold-dark));
  }
  .pink-rule {
    position: absolute; left: 0; top: 37px; width: 100%; height: 11px;
    background: var(--pink);
  }

  .field {
    position: absolute; left: 0; top: 48px; width: 100%; height: 768px;
    background: linear-gradient(180deg, var(--cream) 0%, var(--peach) 35%, var(--amber) 65%, var(--deep-amber) 100%);
    overflow: hidden;
  }
  .comb {
    position: absolute; left: 0; top: 500px; width: 100%; height: 268px;
    background: linear-gradient(180deg, rgba(243,166,64,0) 0%, var(--comb-light) 28%, var(--comb-dark) 100%);
  }
  .hexes { position: absolute; left: 0; top: 0; width: 100%; height: 100%; }

  .bee {
    position: absolute; left: 438px; top: 296px; width: 128px; height: 176px;
    border-radius: 50% 50% 45% 45%;
    background: radial-gradient(ellipse at 50% 40%, #5a3512 0%, #a9702c 50%, rgba(240,200,140,0.5) 80%, rgba(240,200,140,0) 100%);
  }

  .title {
    position: absolute; left: 0; top: 36px; width: 100%;
    text-align: center;
    font-family: "Cinzel", serif; font-weight: 400;
    color: var(--ink);
    font-size: 78px; letter-spacing: 2px; line-height: 1;
  }
  .byline {
    position: absolute; left: 0; top: 114px; width: 100%;
    text-align: center;
    font-family: "Cinzel", serif; color: var(--ink);
    font-size: 46px; letter-spacing: 3px; line-height: 1.2;
  }
  .tagline {
    position: absolute; left: 0; top: 192px; width: 100%;
    text-align: center;
    font-family: "Cinzel", serif; color: var(--rust);
    font-size: 37px; letter-spacing: 2px; line-height: 1.2;
  }

  .foil-bottom {
    position: absolute; left: 0; top: 816px; width: 100%; height: 194px;
    background: linear-gradient(100deg, var(--gold-dark), var(--gold-light) 20%, var(--gold) 45%, var(--gold-light) 70%, var(--gold-dark));
  }
  .name-bar {
    position: absolute; left: 0; top: 837px; width: 100%; height: 50px;
    background: linear-gradient(90deg, var(--bar-dark), var(--bar-light) 50%, var(--bar-dark));
    border-top: 2px solid #e9e2c8; border-bottom: 2px solid #e9e2c8;
    display: flex; align-items: center; justify-content: center;
    font-family: "Federo", sans-serif; color: var(--bar-text);
    font-size: 40px; letter-spacing: 4px; line-height: 1;
  }
</style>
</head>
<body>
  <div class="label">
    <div class="foil-top" role="img" aria-label="Embossed gold foil band"></div>
    <div class="pink-rule"></div>

    <div class="field">
      <div class="comb" role="img" aria-label="Honeycomb cell texture"></div>
      <svg class="hexes" viewBox="0 0 1005 768" aria-hidden="true">
        <g fill="var(--hex)">
          <polygon points="86,432 144,332 260,332 318,432 260,532 144,532"/>
          <polygon points="282,528 340,428 456,428 514,528 456,628 340,628"/>
          <polygon points="482,440 540,340 656,340 714,440 656,540 540,540"/>
          <polygon points="671,544 729,444 845,444 903,544 845,644 729,644"/>
          <polygon points="834,450 892,350 1008,350 1066,450 1008,550 892,550"/>
        </g>
      </svg>
      <div class="bee" role="img" aria-label="Photograph of a honey bee seen from above"></div>
      <h1 class="title">NATURAL HONEY</h1>
      <p class="byline">BY MORTON</p>
      <p class="tagline">GUARANTEED QUALITY</p>
    </div>

    <div class="foil-bottom" role="img" aria-label="Embossed gold foil with floral scroll ornament"></div>
    <div class="name-bar">all natural honey</div>
  </div>
</body>
</html>
```